Modern wordpress-enabled design wanted for translations agency serving large corporations

We are a translation agency and we only work for corporate clients and not private individuals. We are currently using the Larvesk wordpress theme and an upload feature called trobanex. It is important that prospective clients can upload their file. So we need a cool design for that kind of feature. We offer different kinds of translations tailored to the needs or global corporations. Corporate communications translations, legal translations, financial translations, healthcare translations, financial translations, audit translations.

```html
<!DOCTYPE html>
<html lang="en">
<head>
<meta charset="utf-8">
<title>Trobanex Translations</title>
<link rel="stylesheet" href="https://fonts.googleapis.com/css2?family=Roboto+Slab:wght@400;700&family=Open+Sans:wght@400;600;700&display=swap">
<style>
:root{
  --blue:#1d76c4;
  --blue-dark:#17538f;
  --navy:#1c3e66;
  --green:#7ab929;
  --green-dark:#5f9a1a;
  --grey-bg:#eeeeee;
  --text:#555b61;
  --dark:#2a2d31;
  --white:#ffffff;
}
*{box-sizing:border-box;margin:0;padding:0}
html,body{width:1200px;height:2284px;overflow:hidden}
body{position:relative;background:var(--white);font-family:"Open Sans",Arial,sans-serif;color:var(--text)}
.abs{position:absolute}
.slab{font-family:"Roboto Slab",Georgia,serif}

/* header */
.header{left:0;top:0;width:1200px;height:110px;background:var(--white)}
.brand{left:34px;top:34px;display:flex;align-items:center;gap:10px}
.brand-mark{width:22px;height:22px;border-radius:50%;background:var(--green)}
.brand-name{font-family:"Open Sans",Arial,sans-serif;font-weight:700;font-size:34px;color:var(--blue);letter-spacing:1px}
.header-actions{right:40px;top:46px;display:flex;gap:12px}
.btn-small{font-size:11px;font-weight:700;padding:6px 12px;letter-spacing:.5px}
.btn-solid{background:var(--blue);color:var(--white)}
.btn-outline{border:1.5px solid var(--blue);color:var(--blue)}

/* hero */
.hero-photo{left:0;top:110px;width:1200px;height:450px;background:linear-gradient(100deg,#1a6fbb 0%,#3f93d6 45%,#a9cfee 68%,#e3eef8 100%)}
.hero-person{left:780px;top:110px;width:300px;height:450px;background:linear-gradient(180deg,#5a3a2c 0%,#3a2a24 35%,#28272c 100%);border-radius:140px 140px 0 0;opacity:.85}
.nav{left:150px;top:116px;display:flex;height:52px}
.nav a{display:flex;align-items:center;justify-content:center;background:var(--white);color:var(--blue);font-size:13px;font-weight:700;text-decoration:none;padding:0 28px;margin-right:3px;border-radius:0 0 6px 6px;box-shadow:0 2px 4px rgba(0,0,0,.15)}
.nav a.active{background:var(--green);color:var(--white)}
.hero-title{left:40px;top:225px;width:640px;font-weight:700;font-size:46px;line-height:56px;color:var(--white);letter-spacing:1px}
.hero-sub{left:40px;top:362px;width:480px;font-size:22px;line-height:30px;color:var(--white);letter-spacing:.5px}
.hero-btn{left:40px;top:462px;border:2px solid var(--white);color:var(--white);font-size:15px;font-weight:600;padding:9px 18px;letter-spacing:1px}

/* welcome */
.welcome-photo{left:60px;top:590px;width:370px;height:280px;background:linear-gradient(180deg,#f5f5f5 0%,#dfe2e6 60%,#c9cdd3 100%)}
.welcome-title{left:590px;top:672px;font-weight:700;font-size:27px;color:var(--blue);letter-spacing:.5px}
.welcome-text{left:590px;top:722px;width:470px;font-size:14px;line-height:22px;color:var(--text)}

/* services */
.services{left:0;top:890px;width:1200px;height:540px;background:var(--grey-bg)}
.slider-arrow{top:1150px;width:20px;height:40px}
.card{top:950px;width:266px;height:450px;background:var(--white);box-shadow:0 2px 6px rgba(0,0,0,.12)}
.card-photo{position:absolute;left:0;top:0;width:266px;height:175px}
.card-wave{position:absolute;left:0;top:120px}
.card-label{position:absolute;left:16px;top:190px;font-size:14px;font-weight:700;line-height:18px;letter-spacing:.5px}
.card-text{position:absolute;left:16px;top:240px;width:234px;font-size:12.5px;line-height:20px;color:var(--text)}
.card-btn{position:absolute;left:113px;top:386px}

/* why */
.why-title{left:146px;top:1466px;font-weight:700;font-size:30px;line-height:34px;color:var(--blue)}
.why-lead{left:146px;top:1550px;width:420px;font-size:13.5px;font-weight:700;line-height:21px;color:var(--dark)}
.why-text{left:146px;top:1630px;width:420px;font-size:13px;line-height:21px;color:var(--text)}
.video{left:600px;top:1462px;width:340px;height:278px;background:linear-gradient(135deg,#1f2c3a 0%,#34475c 50%,#1a232e 100%)}
.video-play{left:750px;top:1582px}

/* testimonials */
.testimonials{left:0;top:1772px;width:1200px;height:236px;background:linear-gradient(180deg,#3a3d42 0%,#2a2c30 100%)}
.testi-title{left:0;top:1790px;width:1200px;text-align:center;font-weight:700;font-size:28px;color:var(--white);letter-spacing:1px}
.testi-text{left:270px;top:1850px;width:660px;text-align:center;font-size:14px;line-height:22px;color:#e6e6e6}
.avatars{left:522px;top:1944px;display:flex;gap:14px}
.avatar{width:38px;height:38px;border-radius:50%;background:#8a8f96;border:2px solid var(--white)}

/* footer */
.footer{left:0;top:2008px;width:1200px;height:276px;background:#f3f3f3}
.foot-col{top:2030px}
.foot-head{font-size:12px;font-weight:700;color:var(--blue-dark);margin-bottom:10px;letter-spacing:.5px}
.foot-list{list-style:none;font-size:11px;line-height:19px;color:var(--text)}
.foot-list li::before{content:"› ";color:var(--blue)}
.foot-contact p{font-size:11px;line-height:16px;color:var(--text);margin-bottom:8px}
.foot-contact b{display:block;color:var(--blue-dark);font-size:11px}
.news-field{width:250px;height:34px;border:1px solid #cfd3d7;background:var(--white);display:flex;align-items:center;justify-content:space-between;padding-left:10px;font-size:12px;color:#999}
.news-send{width:34px;height:34px;background:var(--blue);display:flex;align-items:center;justify-content:center}
.social{display:flex;gap:7px;margin-top:6px}
.social span{width:24px;height:24px;background:#8fa5bf}
.foot-brand{left:850px;top:2222px;display:flex;align-items:center;gap:8px}
.foot-brand .brand-mark{width:14px;height:14px}
.foot-brand .brand-name{font-size:22px}
</style>
</head>
<body>

<header class="abs header">
  <div class="abs brand"><span class="brand-mark"></span><span class="brand-name">TROBANEX</span></div>
  <div class="abs header-actions">
    <span class="btn-small btn-solid">SUBSCRIBE LOGIN</span>
    <span class="btn-small btn-outline">SIGN UP NOW</span>
  </div>
</header>

<div class="abs hero-photo" role="img" aria-label="Blue office background with financial charts"></div>
<div class="abs hero-person" role="img" aria-label="Businesswoman in dark suit seated at a laptop"></div>
<nav class="abs nav">
  <a class="active">HOME</a><a>ABOUT US</a><a>SERVICES</a><a>LANGUAGE</a><a>CYBER</a><a>BLOG</a><a>CONTACT US</a>
</nav>
<h1 class="abs hero-title slab">INVESTING JUST BECAME EFFORTLES!</h1>
<p class="abs hero-sub slab">LOREM IPSUM DOLOR SIT CONSECTETUR ADIPISCING ELIT</p>
<span class="abs hero-btn">READ MORE</span>

<div class="abs welcome-photo" role="img" aria-label="Businesswoman working at a desk with a laptop"></div>
<h2 class="abs welcome-title slab">WELCOME TO TROBANEX</h2>
<p class="abs welcome-text">We translate contracts, reports and filings for global corporations. Our certified linguists work in over forty languages, and every project passes a second review. Upload your files securely and receive a tailored quote within one business day.</p>

<section class="abs services"></section>
<svg class="abs slider-arrow" style="left:140px" viewBox="0 0 20 40"><path d="M16 4 L4 20 L16 36" fill="none" stroke="#b5b9be" stroke-width="3"/></svg>
<svg class="abs slider-arrow" style="left:1040px" viewBox="0 0 20 40"><path d="M4 4 L16 20 L4 36" fill="none" stroke="#b5b9be" stroke-width="3"/></svg>

<article class="abs card" style="left:175px">
  <div class="card-photo" role="img" aria-label="Business meeting around a large screen" style="background:linear-gradient(160deg,#d9e4ee,#8aa6bf)"></div>
  <svg class="card-wave" width="266" height="60" viewBox="0 0 266 60"><path d="M0 30 Q133 -10 266 30 L266 60 L0 60 Z" fill="#fff"/><path d="M0 30 Q133 -10 266 30" fill="none" stroke="var(--green)" stroke-width="4"/></svg>
  <h3 class="card-label" style="color:var(--green)">LEGAL<br>TRANSLATIONS</h3>
  <p class="card-text">Contracts, patents and court papers translated by sworn legal linguists with strict confidentiality.</p>
  <svg class="card-btn" width="40" height="40" viewBox="0 0 40 40"><circle cx="20" cy="20" r="18" fill="var(--green)"/><path d="M17 12 L25 20 L17 28" fill="none" stroke="#fff" stroke-width="3"/></svg>
</article>

<article class="abs card" style="left:470px">
  <div class="card-photo" role="img" aria-label="Green growth arrow rising over plants" style="background:linear-gradient(160deg,#dfeecb,#6f9a3f)"></div>
  <svg class="card-wave" width="266" height="60" viewBox="0 0 266 60"><path d="M0 30 Q133 -10 266 30 L266 60 L0 60 Z" fill="#fff"/><path d="M0 30 Q133 -10 266 30" fill="none" stroke="var(--blue)" stroke-width="4"/></svg>
  <h3 class="card-label" style="color:var(--blue)">FINANCIAL<br>TRANSLATIONS</h3>
  <p class="card-text">Annual reports, audits and investor updates delivered accurately and on deadline for every market.</p>
  <svg class="card-btn" width="40" height="40" viewBox="0 0 40 40"><circle cx="20" cy="20" r="18" fill="var(--blue)"/><path d="M17 12 L25 20 L17 28" fill="none" stroke="#fff" stroke-width="3"/></svg>
</article>

<article class="abs card" style="left:765px">
  <div class="card-photo" role="img" aria-label="Team of medical professionals" style="background:linear-gradient(160deg,#e8ecf0,#7e8c99)"></div>
  <svg class="card-wave" width="266" height="60" viewBox="0 0 266 60"><path d="M0 30 Q133 -10 266 30 L266 60 L0 60 Z" fill="#fff"/><path d="M0 30 Q133 -10 266 30" fill="none" stroke="var(--blue)" stroke-width="4"/></svg>
  <h3 class="card-label" style="color:var(--blue)">HEALTHCARE<br>TRANSLATIONS</h3>
  <p class="card-text">Clinical studies, labels and patient materials handled by specialists in medical terminology.</p>
  <svg class="card-btn" width="40" height="40" viewBox="0 0 40 40"><circle cx="20" cy="20" r="18" fill="var(--blue)"/><path d="M17 12 L25 20 L17 28" fill="none" stroke="#fff" stroke-width="3"/></svg>
</article>

<h2 class="abs why-title slab">WHY<br>CHOOSE US?</h2>
<p class="abs why-lead">LOREM IPSUM DOLOR SIT AMET, CONSECTETUR ADIPISCING DUIS CONSEQUAT SIT AMET EST A FACILISIS</p>
<p class="abs why-text">Corporate clients choose us for secure file handling, fixed turnaround times and dedicated project managers who know their industry and their terminology.</p>
<div class="abs video" role="img" aria-label="Video still of a business team in a dark office"></div>
<svg class="abs video-play" width="40" height="40" viewBox="0 0 40 40"><circle cx="20" cy="20" r="18" fill="none" stroke="#fff" stroke-width="2.5"/><path d="M16 12 L28 20 L16 28 Z" fill="#fff"/></svg>

<section class="abs testimonials" role="img" aria-label="Dark faded background of business people"></section>
<h2 class="abs testi-title slab">TESTIMONIALS</h2>
<p class="abs testi-text">Lorem ipsum dolor sit amet, consectetur adipiscing elit. Cras suscipit purus vel elementum laoreet. Sed quis diam vitae mauris porta rutrum nec sed feugiat, volutpat mollis ex.</p>
<div class="abs avatars">
  <span class="avatar" role="img" aria-label="Client portrait"></span>
  <span class="avatar" role="img" aria-label="Client portrait"></span>
  <span class="avatar" role="img" aria-label="Client portrait"></span>
</div>

<footer class="abs footer"></footer>
<div class="abs foot-col" style="left:140px">
  <h4 class="foot-head">TROBANEX</h4>
  <ul class="foot-list"><li>Home</li><li>About</li><li>Services</li><li>Language</li><li>Careers</li><li>Blog</li><li>Contact</li></ul>
</div>
<div class="abs foot-col" style="left:310px">
  <h4 class="foot-head">OUR SERVICES</h4>
  <ul class="foot-list"><li>Corporate Communications</li><li>Legal Translations</li><li>Financial Translations</li><li>Healthcare Translations</li><li>Audit Translations</li><li>Technical Translations</li></ul>
</div>
<div class="abs foot-col foot-contact" style="left:520px;width:200px">
  <h4 class="foot-head">CONTACT US</h4>
  <p><b>Address</b>12 Harbor Lane, Suite 4</p>
  <p><b>Phone</b>+1 555 0142 300</p>
  <p><b>Email</b>hello@trobanex.example</p>
</div>
<div class="abs foot-col" style="left:850px">
  <h4 class="foot-head">SUBMIT NEWSLETTER</h4>
  <div class="news-field">Your email<span class="news-send"><svg width="16" height="16" viewBox="0 0 16 16"><path d="M1 8 L15 1 L11 15 L8 9 Z" fill="#fff"/></svg></span></div>
  <h4 class="foot-head" style="margin-top:18px">FOLLOW US</h4>
  <div class="social"><span></span><span></span><span></span><span></span><span></span><span></span></div>
</div>
<div class="abs foot-brand"><span class="brand-mark"></span><span class="brand-name">TROBANEX</span></div>

</body>
</html>
```